2014 Programme

We need a brochure for some training courses we are providing.

All content is available: http://tandrovix.com/academy/tandrovix-academy-programmes-2014

The brochure should be delivered in PDF and will be printed at a later date.

```html
<!DOCTYPE html>
<html lang="en">
<head>
<meta charset="utf-8">
<title>Tandrovix Academy – 2014 Programme</title>
<link href="https://fonts.googleapis.com/css2?family=Raleway:wght@300;400;600;700;800&display=swap" rel="stylesheet">
<style>
:root{
  --stage:#8c8c8c;
  --paper:#efefef;
  --ink:#3a3a3a;
  --pink:#d4266f;
  --bar:#4d4d4d;
  --panel:#5c5c5c;
  --panel-dark:#4a4a4a;
  --white:#ffffff;
  --muted:#cfcfcf;
  --photo-a:#2a2c45;
  --photo-b:#6a6f8c;
}
*{box-sizing:border-box;margin:0;padding:0}
html,body{width:1200px;height:795px;overflow:hidden}
body{background:var(--stage);font-family:"Raleway",sans-serif;color:var(--ink);position:relative}
.brochure{position:absolute;left:320px;top:12px;width:560px;height:771px;background:var(--paper);overflow:hidden;box-shadow:0 4px 14px rgba(0,0,0,.35)}
.hero-photo{position:absolute;left:0;top:0;width:560px;height:118px;background:linear-gradient(100deg,var(--photo-a) 0%,var(--photo-b) 40%,#3c3f5e 65%,var(--photo-b) 100%)}
.testimonials-title{position:absolute;right:0;top:92px;width:218px;height:28px;background:var(--paper);font-weight:800;font-size:22px;letter-spacing:.5px;color:#111;padding:2px 0 0 12px}
.curriculum{position:absolute;left:18px;top:128px;width:318px}
.curriculum h2{font-weight:400;font-size:14px;color:var(--pink);letter-spacing:.4px;margin-bottom:3px}
.lead{font-size:8.5px;color:var(--pink);line-height:1.3;margin-bottom:5px}
.part-bar{background:var(--bar);color:var(--white);font-size:8.5px;font-weight:600;padding:3px 6px;margin:5px 0 4px}
.part-intro{font-size:8.2px;line-height:1.35;color:var(--pink);margin-bottom:5px}
.topics{list-style:disc;padding-left:14px;font-size:8.2px;line-height:1.35;margin-bottom:6px}
.outcome{font-size:8.2px;line-height:1.35;color:var(--pink);margin-bottom:4px}
.side{position:absolute;left:350px;top:124px;width:196px}
.quote{background:var(--panel);color:#e4e4e4;font-size:7.8px;line-height:1.35;padding:6px 8px}
.quote-name{font-size:8.5px;font-weight:700;color:var(--pink);text-transform:uppercase;margin:4px 0 10px;line-height:1.2}
.coach-bar{background:var(--bar);color:var(--white);font-size:8.5px;font-weight:700;padding:3px 6px;margin-top:4px}
.coach-bio{font-size:8.2px;font-weight:700;line-height:1.35;padding:5px 4px}
.coach-panel{position:absolute;left:346px;top:448px;width:214px;height:323px;background:var(--panel-dark);color:var(--white);padding:14px 12px}
.coach-panel p{font-size:8.2px;font-weight:700;line-height:1.35}
.wordmark{position:absolute;left:28px;bottom:150px;font-size:22px;font-weight:400;color:var(--white);line-height:1}
.awards{position:absolute;left:0;top:600px;width:346px;height:171px;background:var(--panel);color:var(--white);padding:14px 18px}
.awards h3{font-weight:400;font-size:11px;line-height:1.2;color:#e6e6e6;margin-bottom:10px}
.award{margin-bottom:9px;line-height:1.2}
.award strong{display:block;font-size:11px;font-weight:700;margin-bottom:2px}
.award span{display:block;font-size:6.5px;color:var(--muted)}
</style>
</head>
<body>
<main class="brochure">
  <div class="hero-photo" role="img" aria-label="Photo of a workshop room with participants watching a presenter"></div>
  <h1 class="testimonials-title">TESTIMONIALS</h1>

  <section class="curriculum">
    <h2>A TWO PART CURRICULUM</h2>
    <p class="lead">We run two courses, each for a business at a different stage in its life-cycle.</p>

    <div class="part-bar">Building Lean Startups: Part 1 / Problem Solution Fit</div>
    <p class="part-intro">This is focused on the first moment of inception as we try to understand how we can solve an actual problem for a real customer with a specific solution.</p>
    <ul class="topics">
      <li>What is a startup?</li>
      <li>The Startup Genome and why startups fail</li>
      <li>Introduction to Lean Startup: Build, measure, learn</li>
      <li>Lean Canvas: the business plan for the lean startup</li>
      <li>Focus: because an unfocused hypothesis is impossible to test</li>
      <li>Innovation Accounting: startup metrics</li>
      <li>How to design and run experiments</li>
      <li>Manual testing and the "Wizard of Oz" technique as tools for customer development</li>
      <li>Lean Pitching Hacks</li>
    </ul>
    <p class="outcome">By the end of the two days, participants understand lean startup principles, have built and pivoted their business model, released a real product to customers (run an experiment) and pitched the business 3 times.</p>

    <div class="part-bar">Building Lean Startups Part 2 / Product Market Fit</div>
    <p class="part-intro">This is focused on businesses that are a few months old, already with problem solution fit, now trying to understand how to build a product that a market wants in a sustainable business model. BLS1 is a prerequisite for this course.</p>
    <ul class="topics">
      <li>Confirming that we have "problem solution fit" – what does it look like?</li>
      <li>Lean Pitching Hacks Part 2</li>
      <li>Communicating traction: Manufacturing forward motion and investor updates</li>
      <li>Backer Roll</li>
      <li>What is product market fit? Systematically working through the "Trough of Sorrow" to success</li>
      <li>Lean Marketing: Growth hacking techniques and best practice</li>
      <li>Innovation Accounting: Startup metrics</li>
    </ul>
    <p class="outcome">By the end of the two days, participants will have strengthened their application of lean startup, signalled their pitch and have a plan to the first 100,000 users with a few experiments already deployed in the market.</p>
  </section>

  <aside class="side">
    <p class="quote">The two days were packed with practical tools we could use straight away. We rebuilt our canvas, ran a live test with real customers and left with a clear plan for the next quarter. Every founder in the room walked out with sharper thinking and a far better pitch than they arrived with.</p>
    <p class="quote-name">– Oren Halvik,<br>Brightfield Advisory</p>
    <p class="quote">A great mix of theory and hands-on work. Our team now tests ideas weekly and talks to customers before writing any code at all.</p>
    <p class="quote-name">– Tobias Renwick,<br>Kestrel9</p>
    <div class="coach-bar">Lean Startup Coach:</div>
    <p class="coach-bio">Marcus Delane is CEO and co-founder of Tandrovix and has started over 25 companies and worked with a few hundred. He has played a big role in new company creation for the likes of Dealbay, Snapsaver, Coinly, 80frocks and Crewly.</p>
  </aside>

  <div class="coach-panel">
    <p>Before Tandrovix, he was the CTO at Sharewave for 5 years and led the development of a technology strategy which saw 5 million users online at any one time, millions of downloads per day and a total global user base of over 100 million.</p>
    <div class="wordmark">tandrovix</div>
  </div>

  <section class="awards">
    <h3>Marcus Delane's Most Recent Industry Awards</h3>
    <div class="award"><strong>Sydney's Most Influential People</strong><span>City business weekly, November 2012</span></div>
    <div class="award"><strong>Australia's Digital Influencers</strong><span>Digital industry review, November 2012</span></div>
    <div class="award"><strong>Top Startup Mentor of 2012</strong><span>Startup community awards</span></div>
  </section>
</main>
</body>
</html>
```